Bluewater Getaways KT needs a new Website

We have an old website that is just that - old. We need a fresh website that is professional graphic designed that has the following features.
1. Can be updated by ourselves in some areas.
2. Has a shopping cart.
3. Has links to download PDF files
4. Has links to other pages in the website
5. Includes social media links
6. Has a client log-in area
Full details in brief provided.

SORRY BUT IT'S URGENT. We've taken too long to write the details and it is now urgent. So my apologies I will be asking for designers to work quickly.

We will continue to use our existing web hosting company and url. Their is a link to the old website in the Design Brief.
Updates

UPDATE:  Please see the new file UPDATE TO DESIGN BRIEF.
Thanks for all your submissions to date.  We hope the update will assist with your designs.
As indicated in previous messages, we are happy with the Home Page + 1 Page in order to select the designer to work with in creating the full design. 

Thankyou Designers.  Much appreciate your efforts.
It's getting late here on Norfolk so I won't have much chance too review any more designs this evening.
But for your information:
Designer 7318405 Ravindra Mehta is so far the closest to what we are seeking.
Thanks again. 

Reason: Have extended to Monday 7 October to give time for designers to submit after feedback today. Especially given the time differences

Target Market(s)

Very wide audience. Current client group not that tech savvy, but we hope to broaden our market and sell more creative products, and so website needs to consider how people now use media, ie tablets & iphones.

Industry/Entity Type

Shopping

Requirements
Nice to have
• PLEASE SEE THE "UPDATE TO THE DESIGN BRIEF"

```html
<!DOCTYPE html>
<html lang="en">
<head>
<meta charset="utf-8">
<title>Bluewater Getaways KT</title>
<link href="https://fonts.googleapis.com/css2?family=Roboto+Condensed:wght@400;700&display=swap" rel="stylesheet">
<style>
:root{
  --page:#2b2b2b;
  --panel:#ffffff;
  --ink:#3a1a0a;
  --muted:#7a7a7a;
  --orange:#f7941d;
  --orange-text:#f28a1a;
  --orange-dark:#e8670e;
  --green:#00a04a;
  --green-dark:#007a36;
  --rule:#cfcfcf;
  --footer-text:#e8e8e8;
}
*{box-sizing:border-box;margin:0;padding:0}
html,body{width:1200px;height:878px;overflow:hidden}
body{background:var(--page);font-family:"Roboto Condensed",Arial,sans-serif;color:var(--ink);position:relative;font-size:13px;letter-spacing:-0.2px}
.panel{position:absolute;background:var(--panel)}
.col-left{left:20px;top:0;width:300px;height:678px}
.col-main{left:330px;top:0;width:540px;height:678px}
.col-side{left:880px;top:0;width:300px;height:678px}

/* news list */
.news{position:absolute;left:10px;top:2px;width:272px}
.news p{font-size:13px;line-height:20px}
.news .loc{color:var(--muted);font-size:12px;text-transform:uppercase;line-height:15px;margin-top:3px}
.news .date{color:var(--muted);font-size:12px;margin-top:4px}
.news .title{color:var(--orange-text);font-size:12.5px;font-weight:700;text-transform:uppercase;margin-top:6px;line-height:18px}
.news hr{border:0;border-top:1px dashed var(--rule);margin-top:4px}
.scrollbar{position:absolute;left:283px;top:0;width:6px;height:224px;background:#ddd;border-radius:3px}
.promo-art{position:absolute;left:10px;top:244px;width:280px;height:423px;background:linear-gradient(180deg,#f5a02a 0%,#c8202e 30%,#b51230 100%)}

/* main */
h1{position:absolute;left:10px;top:-4px;font-size:31px;font-weight:400;color:var(--ink)}
.intro{position:absolute;left:10px;top:42px;width:515px;font-size:13px;line-height:20px;hyphens:auto}
.intro p+p{margin-top:20px}
h2{font-size:21px;font-weight:400;color:var(--ink)}
.promotes h2{position:absolute;left:10px;top:212px}
.bullets{position:absolute;list-style:none;font-size:13px;line-height:20px}
.bullets li{padding-left:10px;position:relative}
.bullets li::before{content:"+";position:absolute;left:0;top:0;font-size:9px;color:#999}
.divider-v{position:absolute;left:260px;top:249px;height:95px;border-left:1px solid var(--rule)}
.supported{position:absolute;left:271px;top:250px;font-size:13px}
.divider-h{position:absolute;left:10px;top:357px;width:518px;border-top:1px dashed var(--rule)}
.brochure-label{position:absolute;left:12px;top:385px;font-size:27px;color:#111}
.btn-download{position:absolute;left:277px;top:377px;width:252px;height:57px;background:linear-gradient(#ffa040,var(--orange-dark));border:1px solid #d65a00;border-radius:3px;color:#3a1a0a;font-size:25px;display:flex;align-items:center;padding-left:16px;gap:8px}
.insurance-art{position:absolute;left:10px;top:455px;width:520px;height:213px;background:linear-gradient(180deg,#dfeef9 0%,#8cc8ee 55%,#5a9a2c 85%,#3f7a20 100%)}

/* side */
.login{position:absolute;left:10px;top:9px;width:280px;height:165px;background:linear-gradient(var(--green),var(--green-dark));border:1px solid #0b6a2f;padding:8px 10px}
.login h2{color:var(--ink);font-size:21px}
.field{display:block;width:260px;height:33px;background:#fff;border:2px solid #d8d8d8;margin-top:10px;font-size:12px;color:#999;padding:7px 8px}
.field:first-of-type{margin-top:11px}
.btn-submit{display:inline-block;margin-top:11px;background:#111;color:#fff;font-size:15px;padding:4px 11px}
.box{position:absolute;left:10px;width:280px;border:1px dashed var(--rule)}
.support{top:184px;height:221px;padding:6px 9px}
.logos{display:grid;grid-template-columns:repeat(3,80px);gap:10px;margin-top:9px}
.logo-slot{height:80px;border:1px solid #e2e2e2;display:flex;align-items:center;justify-content:center;color:#c8c8c8;font-size:21px}
.shop{top:415px;height:251px;padding:6px 9px;background:linear-gradient(#fff,#f3f3f3)}
.item{margin-top:4px}
.item + .item{margin-top:8px}
.item .title{color:var(--orange-text);font-size:12.5px;font-weight:700;text-transform:uppercase}
.item p{font-size:13px;line-height:15px;margin-top:6px;width:250px;hyphens:auto}
.item .row{display:flex;justify-content:space-between;align-items:center;margin-top:10px}
.item .posted{color:var(--muted);font-size:12.5px;padding-left:2px}
.btn-book{background:linear-gradient(#ffa040,var(--orange-dark));border:1px solid #d65a00;color:#3a1a0a;font-size:15px;height:30px;line-height:28px;padding:0 11px}
.item hr{border:0;border-top:1px dashed #bbb;margin-top:8px}

/* footer */
.footer h3{position:absolute;font-size:16px;font-weight:400;color:var(--footer-text)}
.links{position:absolute;list-style:none;font-size:12px;color:var(--footer-text);line-height:13px}
.links li{padding-left:11px;position:relative;margin-bottom:7px}
.links li::before{content:"+";position:absolute;left:0;font-size:8px;color:#999}
.copyright{position:absolute;left:470px;top:760px;font-size:12px;color:var(--footer-text)}
.news-note{position:absolute;left:880px;top:721px;font-size:12px;color:var(--footer-text)}
.email{position:absolute;left:880px;top:745px;width:192px;height:33px;background:#fff;border:2px solid #ccc;font-size:12px;color:#999;padding:8px 12px}
.btn-subscribe{position:absolute;left:1080px;top:746px;width:101px;height:32px;background:linear-gradient(#ffa040,var(--orange-dark));color:#3a1a0a;font-size:15px;display:flex;align-items:center;justify-content:center}
.social{position:absolute;left:880px;top:818px;display:flex;gap:5px}
.social span{width:31px;height:31px;background:var(--orange);display:flex;align-items:center;justify-content:center}
.social span::after{content:"";width:10px;height:10px;border-radius:50%;background:#fff}
</style>
</head>
<body>

<section class="panel col-left">
  <div class="news">
    <p>inclusive. Phuket based.</p>
    <p class="loc">Thailand</p>
    <p class="date">20 November 2013</p>
    <hr>
    <p class="title">New Zealand, South Island February 2013</p>
    <p>See brochure for details.&nbsp; More information available on request.&nbsp; Bookings close 15 January.&nbsp; Indicate interest as soon as possible.&nbsp; Great holiday!</p>
    <p class="loc">New Zealand's South Island, Queenstown, Milford Sound &amp; Christchurch</p>
    <p class="date">25 November 2013</p>
  </div>
  <div class="scrollbar"></div>
  <div class="promo-art" role="img" aria-label="Sunset travel promotion with holiday snapshots: quality supported holidays and travel options"></div>
</section>

<main class="panel col-main">
  <h1>Our Socila Enterprise</h1>
  <div class="intro">
    <p>Bluewater Getaways KT is based in Coral Bay, Queensland and was established in 2001 as Bluewater Coast Supported Holidays. We are Disability Service Providers experienced in the provision of recreation for people with special needs.</p>
    <p>Our services are based on the quality framework and standards set by the Queensland, Victorian and NSW State Government Disability Departments. Bluewater Getaways KT work closely with health, respite and welfare</p>
  </div>
  <div class="promotes"><h2>Promotes</h2></div>
  <ul class="bullets" style="left:10px;top:250px">
    <li>Diversity</li><li>Caring</li><li>Community</li><li>Norfolk Island</li>
  </ul>
  <div class="divider-v"></div>
  <div class="supported">Supported</div>
  <ul class="bullets" style="left:343px;top:250px">
    <li>holidays</li><li>travel</li><li>recreation</li><li>respite</li><li>creative projects</li>
  </ul>
  <div class="divider-h"></div>
  <div class="brochure-label">2013 holidays &amp; travel</div>
  <div class="btn-download">
    <svg width="22" height="28" viewBox="0 0 24 30" aria-hidden="true"><path d="M2 1h14l6 6v22H2z" fill="none" stroke="#3a1a0a" stroke-width="2"/><path d="M16 1v6h6" fill="none" stroke="#3a1a0a" stroke-width="2"/></svg>
    Download Brochure
  </div>
  <div class="insurance-art" role="img" aria-label="Group of travellers with luggage on grass: travel insurance has various options for single or multiple trips"></div>
</main>

<aside class="panel col-side">
  <div class="login">
    <h2>Client login</h2>
    <span class="field">Email</span>
    <span class="field">Password</span>
    <span class="btn-submit">Submit</span>
  </div>
  <div class="box support">
    <h2>Support Us</h2>
    <div class="logos">
      <div class="logo-slot">LOGO</div><div class="logo-slot">LOGO</div><div class="logo-slot">LOGO</div>
      <div class="logo-slot">LOGO</div><div class="logo-slot">LOGO</div><div class="logo-slot">LOGO</div>
    </div>
  </div>
  <div class="box shop">
    <h2>Our Shop</h2>
    <div class="item">
      <div class="title">New Zealand, South Island February 2013</div>
      <p>See brochure for details.&nbsp; More information available on request.&nbsp; Bookings close 15 January.</p>
      <div class="row"><span class="posted">Posted at 23 Dec 2013</span><span class="btn-book">Book Now</span></div>
      <hr>
    </div>
    <div class="item">
      <div class="title">South Island February 2013</div>
      <p>See brochure for details.&nbsp; More information available on request.&nbsp; Bookings close 25 January.</p>
      <div class="row"><span class="posted">Posted at 25 Dec 2013</span><span class="btn-book">Book Now</span></div>
    </div>
  </div>
</aside>

<footer class="footer">
  <h3 style="left:20px;top:694px">Quick links</h3>
  <ul class="links" style="left:20px;top:718px">
    <li>Home</li><li>Governance</li><li>Norfolk Island</li><li>Our Mission &amp; Values</li><li>Services</li><li>Our Facilitators</li><li>Our Shop</li>
  </ul>
  <ul class="links" style="left:160px;top:718px;width:130px">
    <li>Holiday Programs</li><li>Design your own Norfolk Island Holiday</li><li>Open Studio Creative Projects</li><li>Schoolies, Siblings &amp; Family Holidays</li><li>Make a Booking</li>
  </ul>
  <div class="copyright">© 2013. BLUEWATER GETAWAYS KT. ALL RIGHTS RESERVED.</div>
  <h3 style="left:880px;top:694px">Sign Up For Newsletter</h3>
  <div class="news-note">Put your e-mail and click on the envelope button.</div>
  <div class="email">Email</div>
  <div class="btn-subscribe">Subscribe</div>
  <h3 style="left:880px;top:793px">Socail links</h3>
  <div class="social">
    <span aria-label="Social link 1"></span><span aria-label="Social link 2"></span><span aria-label="Social link 3"></span><span aria-label="Social link 4"></span>
  </div>
</footer>

</body>
</html>
```